KT-Systems advertising flag and billboard design

I need a design for advertising flag and a design for billboard.
Information can be obtained from https://kt-sytronik.de.
Updates
Target Market(s)
IT service for companies
Requirements
Must have
- Logo, contact information and services

```html
<!DOCTYPE html>
<html lang="en">
<head>
<meta charset="utf-8">
<title>KT-Systems Billboard</title>
<link rel="stylesheet" href="https://fonts.googleapis.com/css2?family=Bebas+Neue&family=Montserrat:wght@500;600;700&display=swap">
<style>
:root{
  --page:#a9a9a9;
  --navy:#0a3566;
  --navy-deep:#062a52;
  --blue-bright:#1a5ea8;
  --ink:#1d1f24;
  --band:#1f2023;
  --white:#ffffff;
  --icon:#2a5fb8;
  --text-dark:#23262d;
}
*{margin:0;padding:0;box-sizing:border-box}
html,body{width:1003px;height:1200px;overflow:hidden;background:var(--page)}
.billboard{
  position:absolute;left:31px;top:351px;width:1052px;height:557px;
  transform:scale(0.8935);transform-origin:0 0;overflow:hidden;
  box-shadow:6px 8px 14px rgba(0,0,0,.35);background:var(--band);
}
.office-photo{
  position:absolute;left:0;top:0;width:1052px;height:333px;
  background:
    radial-gradient(ellipse 140px 110px at 470px 150px,rgba(255,236,205,.95),rgba(255,236,205,0) 100%),
    radial-gradient(ellipse 260px 60px at 380px 20px,rgba(232,128,50,.55),rgba(232,128,50,0) 100%),
    linear-gradient(180deg,#2c3a4a 0%,#51687e 45%,#8fa9bf 70%,#3c4e60 100%);
}
.corner-shade{position:absolute;left:0;top:0;width:1052px;height:333px}
.brand{
  position:absolute;left:30px;top:28px;
  font-family:"Montserrat",sans-serif;font-weight:700;font-size:22px;
  letter-spacing:2px;color:var(--white);
}
.services-band{position:absolute;left:0;top:333px;width:700px;height:150px;background:var(--white)}
.contact-band{position:absolute;left:0;top:483px;width:1052px;height:74px;background:linear-gradient(90deg,#222327,#2b2c30)}
.blue-panel{position:absolute;left:0;top:0;width:1052px;height:557px}
.service{
  position:absolute;display:flex;align-items:center;gap:10px;
  font-family:"Montserrat",sans-serif;font-weight:600;font-size:13.5px;line-height:1;color:var(--text-dark);
}
.service svg{width:24px;height:24px;flex:none}
.contact{
  position:absolute;top:503px;display:flex;align-items:center;gap:10px;
  font-family:"Bebas Neue",sans-serif;font-weight:400;font-size:29px;color:var(--white);letter-spacing:.5px;
}
.headline{
  position:absolute;right:25px;top:138px;
  font-family:"Bebas Neue",sans-serif;font-weight:400;font-size:86px;line-height:1;color:var(--white);
}
.guarantee{
  position:absolute;right:24px;top:221px;text-align:right;
  font-family:"Montserrat",sans-serif;font-weight:700;font-size:16.5px;line-height:17px;color:var(--white);
}
.tagline{
  position:absolute;left:677px;top:283px;
  font-family:"Bebas Neue",sans-serif;font-weight:400;font-size:42px;line-height:1;color:var(--white);
}
.perk{
  position:absolute;width:160px;text-align:center;
  font-family:"Montserrat",sans-serif;font-weight:500;font-size:12px;line-height:12px;color:var(--white);
}
.perk svg{display:block;margin:0 auto 6px;width:40px;height:40px}
</style>
</head>
<body>
<main class="billboard">
  <div class="office-photo" role="img" aria-label="Photo of a bright modern open-plan office with desks, computer monitors and tall windows"></div>
  <svg class="corner-shade" viewBox="0 0 1052 333" aria-hidden="true">
    <polygon points="0,0 330,0 0,300" fill="rgba(15,20,28,.55)"/>
  </svg>
  <div class="brand">KT-SYSTEMS</div>

  <section class="services-band"></section>
  <div class="contact-band"></div>

  <svg class="blue-panel" viewBox="0 0 1052 557" aria-hidden="true">
    <defs>
      <linearGradient id="panelFill" x1="0" y1="0" x2="1" y2="0.6">
        <stop offset="0" stop-color="#1d63ad"/>
        <stop offset="0.5" stop-color="#0b3c72"/>
        <stop offset="1" stop-color="#052850"/>
      </linearGradient>
    </defs>
    <path d="M727,0 L1052,0 L1052,557 L712,557 L540,365 Q490,300 540,238 Z" fill="url(#panelFill)" stroke="#0b2f5c" stroke-width="4"/>
  </svg>

  <div class="service" style="left:25px;top:354px"><svg viewBox="0 0 24 24" fill="none" stroke="var(--icon)" stroke-width="1.4"><rect x="3" y="4" width="18" height="12" rx="1"/><path d="M1 19h22"/></svg>Laptop Repair</div>
  <div class="service" style="left:25px;top:396px"><svg viewBox="0 0 24 24" fill="none" stroke="var(--icon)" stroke-width="1.4"><circle cx="12" cy="12" r="10"/><path d="M7 14a3 3 0 0 1 1-6 4 4 0 0 1 8 1 2.5 2.5 0 0 1 0 5z"/></svg>Data Backup and<br>Recovery</div>
  <div class="service" style="left:25px;top:444px"><svg viewBox="0 0 24 24" fill="none" stroke="var(--icon)" stroke-width="1.4"><rect x="4" y="6" width="14" height="14"/><rect x="8" y="10" width="6" height="6"/><path d="M18 3v5M15 5h6"/></svg>Hardware Upgrade</div>

  <div class="service" style="left:203px;top:355px"><svg viewBox="0 0 24 24" fill="none" stroke="var(--icon)" stroke-width="1.4"><rect x="3" y="3" width="18" height="12" rx="1"/><path d="M9 21h6M12 15v6"/></svg>PC Repair</div>
  <div class="service" style="left:203px;top:397px"><svg viewBox="0 0 24 24" fill="none" stroke="var(--icon)" stroke-width="1.4"><circle cx="12" cy="12" r="5"/><path d="M12 2v5M12 17v5M2 12h5M17 12h5M5 5l3.5 3.5M15.5 15.5L19 19M19 5l-3.5 3.5M8.5 15.5L5 19"/></svg>Malware and<br>Virus Removal</div>
  <div class="service" style="left:203px;top:444px"><svg viewBox="0 0 24 24" fill="none" stroke="var(--icon)" stroke-width="1.4"><rect x="3" y="3" width="18" height="5"/><rect x="3" y="10" width="18" height="5"/><rect x="3" y="17" width="18" height="5"/></svg>PC Individual</div>

  <div class="service" style="left:353px;top:355px"><svg viewBox="0 0 24 24" fill="none" stroke="var(--icon)" stroke-width="1.4"><rect x="3" y="3" width="18" height="13" rx="1"/><path d="M9 21h6M12 16v5"/><rect x="9" y="7" width="6" height="5"/></svg>Desktop Repair</div>
  <div class="service" style="left:353px;top:398px"><svg viewBox="0 0 24 24" fill="none" stroke="var(--icon)" stroke-width="1.4"><rect x="3" y="3" width="18" height="13" rx="1"/><path d="M9 21h6M12 16v5M12 6v7M9 10l3 3 3-3"/></svg>Software Installation</div>
  <div class="service" style="left:353px;top:444px"><svg viewBox="0 0 24 24" fill="none" stroke="var(--icon)" stroke-width="1.4"><circle cx="12" cy="12" r="10"/><circle cx="12" cy="12" r="3"/><path d="M12 2v7M12 15v7M2 12h7M15 12h7"/></svg>Network / Servers</div>

  <div class="contact" style="left:80px"><svg width="34" height="34" viewBox="0 0 24 24" fill="var(--white)"><path d="M6.6 2.5l3 3.6-1.9 2.2a12 12 0 0 0 8 8l2.2-1.9 3.6 3-2.2 3.3C11.5 20.8 3.2 12.5 3.3 4.7z"/></svg>07731-4826150</div>
  <div class="contact" style="left:354px"><svg width="36" height="28" viewBox="0 0 36 28" fill="none" stroke="var(--white)" stroke-width="3"><rect x="2" y="2" width="32" height="24"/><path d="M2 2l16 15L34 2"/></svg>INFO@KT-SY.DE</div>

  <h1 class="headline">OUR SERVICES</h1>
  <p class="guarantee">All services include a 30-day customer<br>satisfaction guarantee</p>
  <h2 class="tagline">FAST &amp; COMFORT ON SITE</h2>

  <div class="perk" style="left:673px;top:340px"><svg viewBox="0 0 40 40" fill="none" stroke="var(--white)" stroke-width="1.6"><circle cx="22" cy="11" r="6"/><path d="M19 11l2 2 4-4M4 26h6l8 4h10l6-5M10 22l6-1 6 3"/></svg>guarantee</div>
  <div class="perk" style="left:865px;top:340px"><svg viewBox="0 0 40 40" fill="none" stroke="var(--white)" stroke-width="1.6"><circle cx="18" cy="20" r="10"/><circle cx="18" cy="20" r="4"/><path d="M30 10l-8 8M26 8l6 6"/></svg>Fast repair</div>
  <div class="perk" style="left:673px;top:415px"><svg viewBox="0 0 40 40" fill="none" stroke="var(--white)" stroke-width="1.6"><rect x="4" y="7" width="32" height="28" rx="2"/><path d="M4 14h32M11 3v7M29 3v7"/><rect x="9" y="19" width="22" height="9"/></svg>Also on weekends</div>
  <div class="perk" style="left:865px;top:415px"><svg viewBox="0 0 40 40" fill="none" stroke="var(--white)" stroke-width="1.6"><path d="M6 34L30 10M26 6a6 6 0 0 0 8 8M34 34L12 12M8 6l6 6-2 2-6-6z"/></svg>Fast on-site<br>solutions</div>
</main>
</body>
</html>
```